依頼詳細
PC版のTOPページと下層1ページ(採用情報)のデザイン制作をお願いいたします。
サイトマップ、依頼内容詳細.txtをご確認いただき、動画のテイストを参考にシンプルで見やすいデザインで制作いただきたいです。
スムーズな連絡と軽微な修正にご対応いただける方へご依頼をさせていただきたいです。
ターゲットは木材資材・建築資材・家具建具資材などを必要とする建築会社様、家具・建具製造会社様などです。
ページ数
2ページ
希望イメージ
シンプル 複雑
単色 カラフル
暗い 明るい
日常 高級
遊び心 厳粛
未来的 伝統的
女性的 男性的
希望する色
茶系、緑系、グレー系
納品ファイル
• イラストレーター形式 (.ai)
補足説明
納品ファイルはXDも可です。
添付してあるアニメーションにテイストを合わせ、
木の温かみを感じさせるデザインで制作してください。
コーポレートですが、あまり堅くなり過ぎないようにしたいです。
BtoB向けの会社ではありますが、就職などを考えている若い方が見ても、
面白そうな企業だなという印象も与えたいです。
動画ダウンロードURLを新たに添付いたしましたので
そちらからダウンロードをお願い致します。
■ 選んだ理由

爽やかな緑を使ったデザインが良かったです。

■ 提案者全員のお礼・コメント

たくさんのご提案をいただきありがとうございました。

```html
<!DOCTYPE html>
<html lang="ja">
<head>
<meta charset="utf-8">
<title>北森木材株式会社</title>
<link rel="stylesheet" href="https://fonts.googleapis.com/css2?family=Noto+Sans+JP:wght@400;500;700&family=Noto+Serif+JP:wght@600;700&display=swap">
<style>
:root{
  --green:#5e9a5f;
  --green-dark:#2f4a36;
  --brown:#8a7b5e;
  --grey-bg:#efefef;
  --text:#333;
  --muted:#777;
  --white:#fff;
  --wood:#e6c8a2;
}
*{margin:0;padding:0;box-sizing:border-box}
html,body{width:1200px;height:4104px;overflow:hidden}
body{font-family:"Noto Sans JP",sans-serif;color:var(--text);background:var(--white);position:relative;font-size:12px}
section,header,footer{position:absolute;left:0;width:1200px}
.ph{position:absolute}
.title{font-size:28px;letter-spacing:4px;font-weight:500}
.sub{font-size:10px;color:var(--green);margin-top:4px}
.body-text{font-size:11px;line-height:2;color:var(--muted)}
.more{position:absolute;display:flex;align-items:center;justify-content:space-between;width:196px;height:36px;border:1px solid var(--green);background:var(--white);font-size:11px;padding:0 14px;color:var(--text)}
.more::after{content:"";width:20px;height:1px;background:var(--green)}

/* header */
.site-header{top:0;height:60px;z-index:2}
.logo{position:absolute;left:24px;top:18px;font-family:"Noto Serif JP",serif;font-weight:700;font-size:19px;color:var(--text)}
.nav{position:absolute;right:84px;top:12px;display:flex;gap:26px}
.nav a{text-align:center;font-size:11px;font-weight:500;color:var(--text);text-decoration:none}
.nav small{display:block;font-size:8px;color:var(--muted)}
.nav-contact{position:absolute;right:0;top:0;width:72px;height:60px;background:var(--green);color:var(--white);font-size:11px;text-align:center;padding-top:16px}
.nav-contact small{display:block;font-size:8px}

/* hero */
.hero{top:0;height:712px}
.hero-name{position:absolute;left:40px;top:440px;font-size:88px;line-height:1.15;letter-spacing:6px;font-weight:500;color:#111}

/* greeting */
.greeting{top:712px;height:460px;background:var(--grey-bg)}

/* news */
.news{top:1172px;height:448px}
.news-list{position:absolute;left:240px;top:166px;width:680px;list-style:none}
.news-list li{display:flex;align-items:center;gap:24px;height:44px;border-bottom:1px solid #e3e3e3;font-size:11px}
.news-date{width:60px;color:var(--muted)}
.news-tag{width:80px;height:14px;background:var(--brown)}

/* service */
.service-head{top:1620px;height:220px;background:linear-gradient(90deg,#2f5d3b,#6ba56a 55%,#d7e6d2)}
.service-head .title,.service-head .sub{color:var(--white)}
.service-grid{top:1840px;height:700px;display:grid;grid-template-columns:repeat(4,300px);grid-template-rows:repeat(2,350px)}
.svc{position:relative}
.svc-label{position:absolute;left:24px;top:200px;width:252px;height:44px;background:var(--white);display:flex;align-items:center;justify-content:center;font-size:14px;font-weight:700;text-align:center;line-height:1.3}
.svc-desc{position:absolute;left:24px;top:250px;width:252px;font-size:10px;line-height:1.8;color:var(--muted)}

/* products */
.products{top:2540px;height:480px;background:var(--grey-bg)}
.prod-grid{position:absolute;left:280px;top:160px;display:grid;grid-template-columns:repeat(4,144px);column-gap:20px;row-gap:18px}
.prod-grid span{height:36px;background:var(--brown);color:var(--white);font-size:11px;display:flex;align-items:center;justify-content:center}

/* recruit */
.recruit{top:3020px;height:520px}

/* contact */
.contact{top:3540px;height:340px;background:linear-gradient(90deg,#e9cfac,#f1dcc0 50%,#e2c39b)}
.contact-btn{position:absolute;top:210px;height:52px;display:flex;align-items:center;justify-content:center;font-size:16px;font-weight:500}

/* footer */
.site-footer{top:3880px;height:224px;background:var(--green-dark);color:#dfe6df}
.foot-logo{position:absolute;left:260px;top:40px;font-family:"Noto Serif JP",serif;font-weight:700;font-size:18px;color:var(--white)}
.foot-info{position:absolute;left:260px;top:78px;font-size:9px;line-height:1.9}
.foot-links{position:absolute;top:40px;list-style:none;font-size:9px;line-height:2}
.copy{position:absolute;left:0;width:1200px;top:196px;text-align:center;font-size:8px;color:#a9b8ab}
</style>
</head>
<body>

<header class="site-header">
  <div class="logo">北森木材株式会社</div>
  <nav class="nav">
    <a>HOME<small>ホーム</small></a>
    <a>ABOUT<small>会社概要</small></a>
    <a>SERVICE<small>事業内容</small></a>
    <a>PRODUCTS<small>製品紹介</small></a>
    <a>MAKER<small>メーカー</small></a>
    <a>CERTIFICATE<small>認証</small></a>
    <a>RECRUIT<small>採用情報</small></a>
  </nav>
  <div class="nav-contact">CONTACT<small>お問い合わせ</small></div>
</header>

<section class="hero">
  <div class="ph" role="img" aria-label="左側の木のイラスト" style="left:0;top:90px;width:240px;height:620px;background:linear-gradient(#a8cf86,#6f9e5a 60%,#3a3a3a)"></div>
  <div class="ph" role="img" aria-label="右側の木のイラストと舞う葉" style="left:740px;top:70px;width:460px;height:640px;background:linear-gradient(#9fcb7e,#4f8a4a 60%,#333)"></div>
  <div class="hero-name">KITAMORI<br>LUMBER</div>
</section>

<section class="greeting">
  <div style="position:absolute;left:112px;top:72px">
    <div class="title">GREETING</div><div class="sub">ご挨拶</div>
  </div>
  <p class="body-text" style="position:absolute;left:112px;top:156px;width:500px">代表取締役からのご挨拶<br><br>私たちは北の森で育った広葉樹を中心に、確かな品質の木材をお届けしています。建築や家具づくりに携わる皆さまの声に寄り添い、用途に合った材を丁寧に選び抜いてまいります。<br><br>木の温かみを未来へつなぐため、森と人と地域を大切にしながら、これからも誠実なものづくりを続けてまいります。</p>
  <div class="more" style="left:112px;top:348px">ご挨拶</div>
  <div class="ph" role="img" aria-label="積み上げられた丸太の写真" style="left:712px;top:0;width:488px;height:400px;background:linear-gradient(135deg,#c9a478,#8a6a45 60%,#6f8f4e)"></div>
  <div class="ph" role="img" aria-label="緑の葉の飾り" style="left:1010px;top:350px;width:150px;height:90px;background:#8fc36b;border-radius:50%;opacity:.7"></div>
</section>

<section class="news">
  <div style="position:absolute;left:280px;top:80px">
    <div class="title">NEWS</div><div class="sub">新着情報</div>
  </div>
  <ul class="news-list">
    <li><span class="news-date">2021.01.01</span><span class="news-tag"></span><span>新着情報のタイトルが入ります。新着情報のタイトルが入ります。</span></li>
    <li><span class="news-date">2021.01.01</span><span class="news-tag"></span><span>新着情報のタイトルが入ります。新着情報のタイトルが入ります。</span></li>
    <li><span class="news-date">2021.01.01</span><span class="news-tag"></span><span>新着情報のタイトルが入ります。新着情報のタイトルが入ります。</span></li>
  </ul>
  <div class="more" style="left:720px;top:336px">新着情報一覧</div>
  <div class="ph" role="img" aria-label="緑の葉の飾り" style="left:20px;top:240px;width:210px;height:130px;background:#7fb65c;border-radius:50%;opacity:.7"></div>
</section>

<section class="service-head">
  <div style="position:absolute;left:112px;top:70px">
    <div class="title">SERVICE</div><div class="sub" style="color:#e7f1e5">事業内容</div>
  </div>
  <p class="body-text" style="position:absolute;left:112px;top:132px;width:480px;color:#eef5ec">北の森の広葉樹を活かし、製材から加工、販売まで一貫して手がけています。</p>
  <div class="more" style="left:112px;top:250px;border-color:var(--white)">事業内容</div>
  <div class="ph" role="img" aria-label="積み木のような木材ブロックの写真" style="left:800px;top:30px;width:400px;height:190px;background:linear-gradient(135deg,#f2e0c4,#d9b98e)"></div>
</section>

<section class="service-grid">
  <div class="svc"><div class="ph" role="img" aria-label="広葉樹製材の写真" style="inset:0 0 110px 0;background:#c8a67c"></div><div class="svc-label">広葉樹製材</div><p class="svc-desc">道産の広葉樹を丁寧に製材し、用途に合わせた寸法でお届けします。</p></div>
  <div class="svc"><div class="ph" role="img" aria-label="針葉樹製材の写真" style="inset:0 0 110px 0;background:#b98f62"></div><div class="svc-label">針葉樹製材</div><p class="svc-desc">建築用の針葉樹材を安定した品質で、幅広いサイズで揃えています。</p></div>
  <div class="svc"><div class="ph" role="img" aria-label="集成材の写真" style="inset:0 0 110px 0;background:#d3b48a"></div><div class="svc-label">高付加価値材の販売、<br>ランバーコア合板</div><p class="svc-desc">家具や建具向けの高付加価値材と合板を、ご要望に応じてご提案します。</p></div>
  <div class="svc"><div class="ph" role="img" aria-label="積層材の写真" style="inset:0 0 110px 0;background:#a47a50"></div><div class="svc-label">積層材</div><p class="svc-desc">強度と美しさを兼ね備えた積層材を、職人の手で仕上げています。</p></div>
  <div class="svc"><div class="ph" role="img" aria-label="輸入木材の写真" style="inset:0 0 110px 0;background:#c49d6e"></div><div class="svc-label">輸入合板</div><p class="svc-desc">海外の信頼できる産地から、品質を確かめた合板を輸入しています。</p></div>
  <div class="svc"><div class="ph" role="img" aria-label="化粧合板の写真" style="inset:0 0 110px 0;background:#8e6a48"></div><div class="svc-label">化粧合板</div><p class="svc-desc">美しい木目を活かした化粧合板で、空間の質を高めるお手伝いをします。</p></div>
  <div class="svc"><div class="ph" role="img" aria-label="木材製品の写真" style="inset:0 0 110px 0;background:#dcc09a"></div><div class="svc-label">新建材等の販売</div><p class="svc-desc">建築の現場に必要な新建材を幅広く取り扱い、迅速にお届けします。</p></div>
  <div class="svc"><div class="ph" role="img" aria-label="倉庫に並ぶ木材の写真" style="inset:0 0 110px 0;background:#b08458"></div></div>
</section>

<section class="products">
  <div style="position:absolute;left:280px;top:72px">
    <div class="title">PRODUCTS</div><div class="sub">製品紹介</div>
  </div>
  <div class="prod-grid">
    <span>製品名</span><span>製品名</span><span>製品名</span><span>製品名</span>
    <span>製品名</span><span>製品名</span><span>製品名</span><span>製品名</span>
    <span>製品名</span><span>製品名</span><span>製品名</span><span>製品名</span>
  </div>
  <div class="more" style="left:720px;top:380px">製品一覧</div>
</section>

<section class="recruit">
  <div class="ph" role="img" aria-label="作業着姿の社員の写真" style="left:48px;top:20px;width:552px;height:450px;background:linear-gradient(135deg,#cfe3b8,#8fb86f)"></div>
  <div class="ph" role="img" aria-label="緑の葉の飾り" style="left:920px;top:0;width:220px;height:150px;background:#7fb65c;border-radius:50%;opacity:.7"></div>
  <div style="position:absolute;left:664px;top:168px">
    <div class="title">RECRUIT</div><div class="sub">採用情報</div>
  </div>
  <p class="body-text" style="position:absolute;left:664px;top:240px;width:420px">森の恵みを未来へつなぐ仲間を募集しています。木が好きな方、ものづくりに興味のある方、まずは気軽にご応募ください。<br><br>経験は問いません。先輩たちが一から丁寧に教えますので、安心して新しい一歩を踏み出してください。</p>
  <div class="more" style="left:880px;top:408px">採用情報</div>
</section>

<section class="contact">
  <div style="position:absolute;left:0;width:1200px;top:80px;text-align:center">
    <div class="title">CONTACT</div><div class="sub">お問い合わせ</div>
  </div>
  <p class="body-text" style="position:absolute;left:280px;top:170px;color:var(--text)">お気軽にお問い合わせください。</p>
  <div class="contact-btn" style="left:280px;width:300px;background:var(--green);color:var(--white)">お問い合わせ</div>
  <div class="contact-btn" style="left:600px;width:320px;background:var(--white);color:var(--green)">TEL: 000-000-0000</div>
</section>

<footer class="site-footer">
  <div class="foot-logo">北森木材株式会社</div>
  <p class="foot-info">〒000-0000 北海道〇〇市〇〇町0丁目0番0号<br>TEL: 000-000-0000<br>FAX: 000-000-0000</p>
  <ul class="foot-links" style="left:600px"><li>ホーム</li><li>会社概要</li><li>事業内容</li><li>製品紹介</li><li>メーカー</li></ul>
  <ul class="foot-links" style="left:780px"><li>認証</li><li>採用情報</li><li>お問い合わせ</li><li>プライバシーポリシー</li></ul>
  <div class="copy">©2021 北森木材株式会社</div>
</footer>

</body>
</html>
```